Design Book Cover - Win The Hiring Room

Need assistance designing a compelling cover for an eBook titled "Win The Hiring Room". eBook is a hard hitting, direct tutorial for how to succeed in a job interview. Written by Derek Pollfrey, a senior partner with 20 years interviewing people for employment at one of the largest and most prestigious consulting firms in the world.

Target Market(s)

anyone looking to land a corporate job with Summit 1000 companies

Industry/Entity Type

Consulting

```html
<!DOCTYPE html>
<html lang="en">
<head>
<meta charset="utf-8">
<title>Win The Hiring Room — Derek Pollfrey</title>
<link rel="stylesheet" href="https://fonts.googleapis.com/css2?family=Bebas+Neue&family=EB+Garamond:wght@500&display=swap">
<style>
  :root {
    --blue-deep: #033c6e;
    --blue-mid: #0563a8;
    --blue-glow: #0a7fd4;
    --title-navy: #023c70;
    --paper: #ffffff;
    --paper-edge: #e3e5e8;
    --ink: #111111;
    --title-white: #fdf9fa;
    --silhouette: #050505;
  }
  html, body {
    margin: 0;
    padding: 0;
    width: 800px;
    height: 1200px;
    overflow: hidden;
    background: var(--paper);
  }
  .cover {
    position: relative;
    width: 800px;
    height: 1200px;
    overflow: hidden;
    background: radial-gradient(ellipse 70% 60% at 40% 70%, var(--paper) 0%, var(--paper) 40%, var(--paper-edge) 100%);
  }
  .cover__sky {
    position: absolute;
    left: 0; top: 0;
    width: 800px; height: 522px;
    background: radial-gradient(ellipse 62% 70% at 46% 46%, var(--blue-glow) 0%, var(--blue-mid) 45%, var(--blue-deep) 100%);
  }
  .cover__title {
    position: absolute;
    left: 0; top: 0;
    width: 800px; height: 700px;
  }
  .cover__title text {
    font-family: "Bebas Neue", "Oswald", sans-serif;
  }
  .title__lead { fill: var(--title-white); }
  .title__main { fill: var(--title-navy); }
  .cover__author {
    position: absolute;
    left: 44px;
    top: 948px;
    margin: 0;
    font-family: "EB Garamond", "Garamond", serif;
    font-weight: 500;
    font-variant: small-caps;
    font-size: 100px;
    line-height: 104px;
    color: var(--ink);
    letter-spacing: 0;
  }
  .cover__author span { display: block; }
  .cover__figure {
    position: absolute;
    left: 493px;
    top: 709px;
    width: 307px;
    height: 478px;
    background: linear-gradient(180deg, #1a1a1a 0%, var(--silhouette) 60%);
    border-radius: 120px 40px 0 0;
  }
  .cover__footer-band {
    position: absolute;
    left: 0; bottom: 0;
    width: 800px; height: 13px;
    background: linear-gradient(90deg, var(--blue-deep) 0%, var(--blue-glow) 55%, var(--blue-deep) 100%);
  }
</style>
</head>
<body>
  <main class="cover">
    <div class="cover__sky"></div>

    <svg class="cover__title" viewBox="0 0 800 700" aria-label="Win The Hiring Room">
      <text class="title__lead" x="766" y="470" text-anchor="end" font-size="230">WIN THE</text>
      <text class="title__main" x="35" y="681" font-size="211" textLength="737" lengthAdjust="spacingAndGlyphs">HIRING ROOM</text>
    </svg>

    <div class="cover__figure" role="img" aria-label="Silhouette of a businessman in a suit and tie"></div>

    <p class="cover__author">
      <span>Derek</span>
      <span>Pollfrey</span>
    </p>

    <div class="cover__footer-band"></div>
  </main>
</body>
</html>
```